Dorin Commercial Truck / Trailer / RV Repair

Need a billboard design for our shop. Will include our logo below and want the word DORIN on the top without the circle. Straighten out the letter "M" on the logo as well. Also will include a rough draft of a design and words I had in mind. All the words need to be included but the layout and design is up to you. Open to all options just needs to be easy to see and understand the message from the highway.

```html
<!DOCTYPE html>
<html lang="en">
<head>
<meta charset="utf-8">
<title>Dorin Commercial Repair Shop – Billboard</title>
<link rel="stylesheet" href="https://fonts.googleapis.com/css2?family=Montserrat:wght@300;400;700;800&display=swap">
<style>
  :root {
    --brand-blue: #2b8ee6;
    --brand-gray: #646363;
    --ink-white: #ffffff;
    --page-bg: #d2d3d5;
    --photo-top: #eef2f5;
    --photo-mid: #8fa7ba;
    --photo-deep: #3d5a72;
    --studio-light: #f7f7f7;
    --studio-shade: #dcdcdc;
    --dock-light: #c9ccd0;
    --dock-dark: #4b4f55;
    --dusk-light: #7d7f92;
    --dusk-dark: #2a2c3a;
  }
  html, body {
    margin: 0;
    width: 1137px;
    height: 1200px;
    overflow: hidden;
    background: var(--page-bg);
  }
  .billboard {
    position: absolute;
    left: 20px;
    top: 380px;
    width: 1097px;
    height: 439px;
    display: block;
    font-family: "Montserrat", sans-serif;
  }
  .board-face { fill: var(--ink-white); }
  .accent-stripe, .tag-blue, .bar-blue, .available-box { fill: var(--brand-blue); }
  .tag-gray, .bar-gray { fill: var(--brand-gray); }
  .wordmark { fill: var(--brand-blue); font-weight: 700; font-size: 106px; }
  .headline-top { fill: var(--brand-gray); font-weight: 800; font-size: 82px; }
  .headline-bottom { fill: var(--brand-blue); font-weight: 800; font-size: 82px; }
  .tag-label { fill: var(--ink-white); font-weight: 800; font-size: 29px; }
  .call-text { fill: var(--ink-white); font-size: 40px; }
  .call-text .light { font-weight: 400; }
  .call-text .strong { font-weight: 800; }
  .or-label { fill: var(--ink-white); font-weight: 800; font-size: 38px; }
  .quote-text { fill: var(--ink-white); font-weight: 400; font-size: 40px; }
  .parking-text { fill: var(--brand-gray); font-weight: 800; font-size: 47px; }
  .available-text { fill: var(--ink-white); font-weight: 800; font-size: 47px; }
  .phone-icon { fill: none; stroke: var(--ink-white); stroke-width: 4; stroke-linecap: round; stroke-linejoin: round; }
</style>
</head>
<body>
<svg class="billboard" viewBox="0 0 1520 608" xmlns="http://www.w3.org/2000/svg">
  <defs>
    <linearGradient id="hero-fill" x1="0" y1="0" x2="0" y2="1">
      <stop offset="0" stop-color="var(--ink-white)"/>
      <stop offset="0.2" stop-color="var(--photo-top)"/>
      <stop offset="0.55" stop-color="var(--photo-mid)"/>
      <stop offset="1" stop-color="var(--photo-deep)"/>
    </linearGradient>
    <linearGradient id="studio-fill" x1="0" y1="0" x2="1" y2="1">
      <stop offset="0" stop-color="var(--studio-light)"/>
      <stop offset="1" stop-color="var(--studio-shade)"/>
    </linearGradient>
    <linearGradient id="dock-fill" x1="0" y1="0" x2="0" y2="1">
      <stop offset="0" stop-color="var(--dock-light)"/>
      <stop offset="1" stop-color="var(--dock-dark)"/>
    </linearGradient>
    <linearGradient id="dusk-fill" x1="0" y1="0" x2="0" y2="1">
      <stop offset="0" stop-color="var(--dusk-light)"/>
      <stop offset="1" stop-color="var(--dusk-dark)"/>
    </linearGradient>
  </defs>

  <rect class="board-face" x="0" y="0" width="1520" height="608"/>

  <!-- hero area -->
  <polygon points="0,110 515,110 288,608 0,608" fill="url(#hero-fill)" role="img" aria-label="Photo of a blue semi truck driving on a highway with snowy mountains behind"/>
  <polygon class="accent-stripe" points="565,0 583,0 305,608 288,608"/>

  <!-- name -->
  <text class="wordmark" x="64" y="215" textLength="386" lengthAdjust="spacingAndGlyphs">DORIN</text>

  <!-- headline -->
  <text class="headline-top" x="730" y="102" textLength="562" lengthAdjust="spacingAndGlyphs">COMMERCIAL</text>
  <text class="headline-bottom" x="728" y="177" textLength="566" lengthAdjust="spacingAndGlyphs">REPAIR SHOP</text>

  <!-- service tags -->
  <polygon class="tag-blue" points="500,196 830,196 815,246 485,246"/>
  <polygon class="tag-gray" points="840,196 1205,196 1190,246 823,246"/>
  <polygon class="tag-blue" points="1215,196 1495,196 1495,246 1200,246"/>
  <text class="tag-label" x="658" y="232" text-anchor="middle">TRUCKS</text>
  <text class="tag-label" x="1015" y="232" text-anchor="middle">TRAILERS</text>
  <text class="tag-label" x="1345" y="232" text-anchor="middle">RV</text>

  <!-- service images -->
  <rect x="446" y="262" width="294" height="146" fill="url(#studio-fill)" role="img" aria-label="Photo of a white semi truck cab"/>
  <polygon points="815,262 1175,262 1110,408 750,408" fill="url(#dock-fill)" role="img" aria-label="Photo of white trailers parked at loading docks"/>
  <polygon points="1185,262 1495,262 1495,408 1125,408" fill="url(#dusk-fill)" role="img" aria-label="Photo of a camper van RV parked at dusk with camping chairs"/>

  <!-- contact bar -->
  <polygon class="bar-blue" points="405,430 895,430 870,488 388,488"/>
  <polygon class="bar-gray" points="902,430 990,430 965,488 877,488"/>
  <polygon class="bar-blue" points="995,430 1520,430 1520,488 970,488"/>
  <path class="phone-icon" d="M440 449 q-4 2 -3 8 q2 10 9 18 q4 3 8 1 l1 -5 l-5 -4 l-3 2 q-4 -4 -6 -10 l3 -2 l-1 -6 z"/>
  <text class="call-text" x="462" y="474"><tspan class="light">CALL </tspan><tspan class="strong">888 555 0142</tspan></text>
  <text class="or-label" x="933" y="473" text-anchor="middle">OR</text>
  <text class="quote-text" x="1245" y="472" text-anchor="middle">Come by for a Quote!</text>

  <!-- parking line -->
  <text class="parking-text" x="515" y="558" textLength="588" lengthAdjust="spacingAndGlyphs">PARKING AND STORAGE</text>
  <rect class="available-box" x="1112" y="515" width="286" height="51"/>
  <text class="available-text" x="1118" y="558" textLength="274" lengthAdjust="spacingAndGlyphs">AVAILABLE</text>
</svg>
</body>
</html>
```